Regional Consulting Business Needs a Business Card Design

We need a business card design for our new business based in Regional Victoria, Australia called Velor Power. We are a consulting company with our main goal being to save people momey money and reducing their carbon footprint. Anything from water saving showerheads, to energy saving lightglobes and even to solar power. We would like to see designs that use bright colours. The final design should shout 'we are here to help you'.

Industry/Entity Type

Business

```html
<!DOCTYPE html>
<html lang="en">
<head>
<meta charset="utf-8">
<title>Velor Power — Business Card</title>
<link rel="stylesheet" href="https://fonts.googleapis.com/css2?family=Arimo:wght@400;700&family=Noto+Serif:ital,wght@1,700&display=swap">
<style>
  :root {
    --page: #e6e4df;
    --card-light: #f6f5f1;
    --card-light-2: #e8e6df;
    --charcoal: #3a3b3e;
    --charcoal-2: #5b5c60;
    --orange: #f39a1b;
    --yellow: #ffc93c;
    --ink: #2f3033;
    --white: #ffffff;
  }
  * { box-sizing: border-box; margin: 0; padding: 0; }
  html, body { width: 1200px; height: 900px; overflow: hidden; }
  body {
    background: var(--page);
    font-family: "Arimo", Arial, sans-serif;
    color: var(--ink);
    position: relative;
  }
  .card {
    position: absolute;
    border-radius: 22px;
    overflow: hidden;
    box-shadow: 0 6px 18px rgba(0,0,0,.18);
  }
  .card-back { left: 560px; top: 70px; width: 560px; height: 320px; background: var(--white); }
  .card-front { left: 80px; top: 470px; width: 620px; height: 355px; }
  .card-art { position: absolute; inset: 0; width: 100%; height: 100%; }

  .brand { display: flex; align-items: center; gap: 10px; }
  .brand-mark { width: 26px; height: 26px; background: var(--orange); }
  .brand-name { font-weight: 700; font-size: 30px; color: var(--charcoal); letter-spacing: .5px; }
  .tagline {
    font-family: "Noto Serif", Georgia, serif;
    font-style: italic; font-weight: 700;
    font-size: 13px; color: var(--ink);
    margin-top: 4px; margin-left: 36px;
  }

  /* back */
  .back-brand { position: absolute; left: 118px; top: 34px; }
  .back-brand .brand-name { font-size: 26px; }
  .back-brand .brand-mark { width: 22px; height: 22px; }
  .back-brand .tagline { font-size: 11px; margin-left: 32px; }
  .services {
    position: absolute; left: 70px; top: 112px; width: 330px;
    list-style: none; text-align: center;
    color: var(--orange); font-size: 10px; text-transform: uppercase; line-height: 1.35;
  }
  .services li + li::before {
    content: ""; display: block; width: 5px; height: 5px;
    background: var(--orange); margin: 9px auto 7px;
  }
  .back-url { position: absolute; right: 36px; top: 196px; font-size: 15px; color: var(--ink); }

  /* front */
  .front-brand { position: absolute; left: 56px; top: 150px; }
  .person { position: absolute; left: 440px; top: 72px; }
  .person-name { color: var(--orange); font-size: 24px; }
  .person-role { color: var(--white); font-size: 14px; letter-spacing: .8px; margin-top: 3px; }
  .address { position: absolute; left: 44px; top: 262px; font-size: 17px; line-height: 1.2; color: var(--ink); }
  .divider { position: absolute; left: 300px; top: 258px; width: 2px; height: 72px; background: var(--orange); }
  .contacts { position: absolute; left: 318px; top: 256px; list-style: none; font-size: 17px; line-height: 1.15; }
  .contacts li { display: flex; align-items: center; gap: 12px; height: 19px; }
  .contacts svg { width: 14px; height: 14px; flex: none; }
</style>
</head>
<body>

<section class="card card-back" aria-label="Business card back">
  <div class="brand-block back-brand">
    <div class="brand"><span class="brand-mark"></span><span class="brand-name">Velor Power</span></div>
    <p class="tagline">Maintenance and consulting services</p>
  </div>
  <ul class="services">
    <li>Energy audits for homes and small business</li>
    <li>Water saving showerheads, efficient lighting and smart fittings for every room</li>
    <li>Solar power design and installation</li>
    <li>Lower bills, smaller carbon footprint, local support</li>
  </ul>
  <p class="back-url">www.velorpower.com</p>
</section>

<section class="card card-front" aria-label="Business card front">
  <svg class="card-art" viewBox="0 0 620 355" preserveAspectRatio="none" aria-hidden="true">
    <defs>
      <linearGradient id="paper" x1="0" y1="0" x2="1" y2="1">
        <stop offset="0" stop-color="#fbfaf7"/>
        <stop offset="1" stop-color="#e6e4dc"/>
      </linearGradient>
      <linearGradient id="panel" x1="0" y1="0" x2="1" y2="0">
        <stop offset="0" stop-color="#6a6b6f"/>
        <stop offset=".5" stop-color="#45464a"/>
        <stop offset="1" stop-color="#333437"/>
      </linearGradient>
    </defs>
    <rect width="620" height="355" fill="url(#paper)"/>
    <path d="M0 28 C200 -8 330 62 420 118 C500 166 560 192 620 198 L620 0 L0 0 Z" fill="url(#panel)"/>
    <path d="M0 38 C200 4 330 74 420 132 C500 180 560 204 620 210" fill="none" stroke="#f39a1b" stroke-width="5"/>
    <path d="M0 48 C190 16 320 90 410 150 C490 196 560 216 620 220" fill="none" stroke="#f39a1b" stroke-width="1.5"/>
    <path d="M120 26 C230 14 320 48 380 82" fill="none" stroke="#ffc93c" stroke-width="2"/>
  </svg>

  <div class="brand-block front-brand">
    <div class="brand"><span class="brand-mark"></span><span class="brand-name">Velor Power</span></div>
    <p class="tagline">Maintenance and consulting services</p>
  </div>

  <div class="person">
    <p class="person-name">Dana Whitfield</p>
    <p class="person-role">GENERAL MANAGER</p>
  </div>

  <address class="address" style="font-style:normal">Level 2, 48 Ridgeline Rd.<br>Ballan Vale, Victoria 3342</address>
  <span class="divider"></span>
  <ul class="contacts">
    <li><svg viewBox="0 0 14 14"><path d="M2 4 C2 2 3 1 7 1 C11 1 12 2 12 4 L10 5 L9 3.5 L5 3.5 L4 5 Z M3 6 L11 6 L12 12 L2 12 Z" fill="#f39a1b"/></svg>+123 555 0142</li>
    <li><svg viewBox="0 0 14 14"><rect x="1" y="1" width="12" height="12" rx="2" fill="#f39a1b"/><rect x="4" y="3" width="6" height="4" fill="#fff"/><rect x="4" y="9" width="6" height="1.5" fill="#fff"/></svg>+123 555 0142</li>
    <li><svg viewBox="0 0 14 14"><rect x="1" y="3" width="12" height="9" fill="#f39a1b"/><path d="M1 3 L7 8 L13 3" fill="none" stroke="#fff" stroke-width="1.2"/></svg>info@velorpower.com</li>
    <li><svg viewBox="0 0 14 14"><circle cx="7" cy="7" r="6" fill="#f39a1b"/><path d="M1 7 H13 M7 1 C4 4 4 10 7 13 M7 1 C10 4 10 10 7 13" fill="none" stroke="#fff" stroke-width=".9"/></svg>www.velorpower.com</li>
  </ul>
</section>

</body>
</html>
```